Building business client journey document

We want to design a journey document which helps our clients understand the process of building a house from initial conversations through to construction. I have attached an example along with the design of stages/writing we would like for ours.

```html
<!DOCTYPE html>
<html lang="en">
<head>
<meta charset="utf-8">
<title>Client Journey – Building Process</title>
<link rel="stylesheet" href="https://fonts.googleapis.com/css2?family=Open+Sans:wght@400;600;700&display=swap">
<style>
  :root {
    --page: #ffffff;
    --poster: #aaa37e;
    --house-edge: #ffffff;
    --house-light: #e8e8e8;
    --house-dark: #c6c6c6;
    --card-back: #bdbdbd;
    --card-inner: #d2d2d2;
    --ink: #333333;
    --ink-dark: #1e1e1e;
    --label-bg: #111111;
    --label-text: #ffffff;
    --design: #f3a81e;
    --design-tag: #f7c52a;
    --preliminary: #2fe0c0;
    --construction: #e8325f;
    --arrow: #f6b619;
    --logo-tab: #dedede;
    --logo-text: #8a8a8a;
  }
  html, body {
    margin: 0;
    padding: 0;
    overflow: hidden;
  }
  .canvas {
    position: relative;
    width: 1200px;
    height: 1200px;
    background: var(--page);
    overflow: hidden;
    font-family: "Open Sans", sans-serif;
  }
  .journey {
    position: absolute;
    left: 257px;
    top: 0;
    width: 685px;
    height: 1200px;
  }
  .poster-bg { fill: var(--poster); }
  .house { fill: url(#houseShade); stroke: var(--house-edge); stroke-width: 6; stroke-linejoin: miter; }
  .logo-tab { fill: var(--logo-tab); }
  .logo-text { fill: var(--logo-text); font-size: 5.2px; font-weight: 400; text-anchor: middle; letter-spacing: 0.2px; }
  .phase-title { fill: var(--ink); font-weight: 400; }
  .phase-tag-text { font-weight: 600; font-size: 10px; text-anchor: middle; }
  .tag-design { fill: var(--design-tag); }
  .tag-preliminary { fill: var(--preliminary); }
  .tag-construction { fill: var(--construction); }
  .tag-text-dark { fill: var(--ink); }
  .tag-text-light { fill: #ffffff; }
  .guide { fill: none; stroke: #555; stroke-width: 0.8; stroke-dasharray: 1 1.2; }
  .frame-design { color: var(--design); }
  .frame-preliminary { color: var(--preliminary); }
  .frame-construction { color: var(--construction); }
  .step-label-box { fill: var(--label-bg); }
  .step-label { fill: var(--label-text); font-size: 3.6px; font-weight: 600; text-anchor: middle; letter-spacing: 0.1px; }
  .step-copy { fill: var(--ink); font-size: 3.3px; text-anchor: middle; }
  .flow-arrow { fill: var(--arrow); }
  .icon-fill { fill: var(--ink-dark); }
  .icon-line { fill: #f2f2f2; stroke: var(--ink-dark); stroke-width: 1.1; stroke-linejoin: round; }
  .icon-stroke { fill: none; stroke: var(--ink-dark); stroke-width: 0.9; stroke-linecap: round; stroke-linejoin: round; }
</style>
</head>
<body>
<div class="canvas">
  <svg class="journey" viewBox="195 82 327 573" xmlns="http://www.w3.org/2000/svg" aria-label="Client journey from initial design to construction">
    <defs>
      <radialGradient id="houseShade" cx="50%" cy="50%" r="60%">
        <stop offset="0%" stop-color="var(--house-light)"/>
        <stop offset="100%" stop-color="var(--house-dark)"/>
      </radialGradient>
      <pattern id="stripes" width="4" height="4" patternUnits="userSpaceOnUse" patternTransform="rotate(45)">
        <rect width="4" height="4" fill="#ffffff"/>
        <rect width="2" height="4" fill="var(--preliminary)"/>
      </pattern>
      <symbol id="stepCard" viewBox="0 0 62 50">
        <rect x="0" y="0" width="62" height="50" rx="8" fill="var(--card-back)"/>
        <rect x="3" y="2.5" width="56" height="44" rx="6" fill="var(--card-inner)"/>
        <path d="M14 38 H50 a4 4 0 0 0 4 -4 V12 a4 4 0 0 0 -4 -4 H14 a4 4 0 0 0 -4 4 V27" fill="none" stroke="currentColor" stroke-width="4" stroke-linecap="round"/>
      </symbol>
    </defs>

    <rect class="poster-bg" x="195" y="82" width="327" height="573"/>

    <polygon class="house" points="203,193 358,96 514,188 505,188 505,646 213,646 213,193"/>

    <g class="brand-tab">
      <rect class="logo-tab" x="416" y="97" width="78" height="63"/>
      <text class="logo-text" x="455" y="124">CORVALE LOGO</text>
      <text class="logo-text" x="455" y="131">+ DETAILS</text>
    </g>

    <!-- Design phase -->
    <g class="phase-heading">
      <text class="phase-title" x="293" y="141" font-size="12">INITIAL</text>
      <text class="phase-title" x="278" y="159" font-size="18" textLength="62" lengthAdjust="spacingAndGlyphs">Design</text>
      <rect class="tag-design" x="342" y="146" width="46" height="14"/>
      <text class="phase-tag-text tag-text-dark" x="365" y="156.5">PHASE</text>
      <path class="guide" d="M389 153 H404 V166"/>
    </g>

    <g class="step" transform="translate(232,172)">
      <use href="#stepCard" class="frame-design" width="62" height="50"/>
      <path class="icon-fill" transform="translate(31,23)" d="M-5 -7 c-2 0 -3 1 -3 3 c0 7 6 13 13 13 c2 0 3 -1 3 -3 l-3 -3 l-3 2 c-2 -1 -4 -3 -5 -5 l2 -3 z"/>
      <rect class="step-label-box" x="11" y="44" width="40" height="17"/>
      <text class="step-label" x="31" y="51">INITIAL</text>
      <text class="step-label" x="31" y="56.5">CONTACT</text>
      <text class="step-copy" x="31" y="67">
        <tspan x="31">A quick chat by phone or email to</tspan>
        <tspan x="31" dy="4.3">learn about your plans, then we send</tspan>
        <tspan x="31" dy="4.3">a short questionnaire so we can see</tspan>
        <tspan x="31" dy="4.3">if we are a good match to work</tspan>
        <tspan x="31" dy="4.3">together.</tspan>
      </text>
    </g>
    <polygon class="flow-arrow" transform="translate(306,194)" points="0,-3.5 6,0 0,3.5"/>
    <g class="step" transform="translate(326,172)">
      <use href="#stepCard" class="frame-design" width="62" height="50"/>
      <g class="handshake-icon" transform="translate(31,23)">
        <path class="icon-fill" d="M-14 -5 L-10 -8 L-7 -3 L-11 0 Z"/>
        <path class="icon-fill" d="M14 -5 L10 -8 L7 -3 L11 0 Z"/>
        <path class="icon-line" d="M-8 -5 L-3 -7 L2 -6 L8 -4 L9 -1 L4 4 L1 6 L-2 5 L-6 2 L-9 -1 Z"/>
        <path class="icon-stroke" d="M2 -6 L-3 -2 L-1 0 L3 -3 M-5 1 L-2 -1 M-3 3 L0 1 M-1 5 L2 3"/>
      </g>
      <rect class="step-label-box" x="11" y="44" width="40" height="17"/>
      <text class="step-label" x="31" y="51">INITIAL</text>
      <text class="step-label" x="31" y="56.5">FACE TO FACE</text>
      <text class="step-copy" x="31" y="67">
        <tspan x="31">Here we sit down to go deeper into</tspan>
        <tspan x="31" dy="4.3">your project and talk about how we</tspan>
        <tspan x="31" dy="4.3">can help you.</tspan>
      </text>
    </g>
    <polygon class="flow-arrow" transform="translate(398,194)" points="0,-3.5 6,0 0,3.5"/>
    <g class="step" transform="translate(418,172)">
      <use href="#stepCard" class="frame-design" width="62" height="50"/>
      <rect class="step-label-box" x="11" y="44" width="40" height="17"/>
      <text class="step-label" x="31" y="51">1ST BASE PAIDS</text>
      <text class="step-label" x="31" y="56.5">ESTIMATE</text>
      <text class="step-copy" x="31" y="67">
        <tspan x="31">At this stage we give you a first</tspan>
        <tspan x="31" dy="4.3">estimate based on our early talks,</tspan>
        <tspan x="31" dy="4.3">so we can deliver the best possible</tspan>
        <tspan x="31" dy="4.3">home for your budget (2-3 days).</tspan>
      </text>
    </g>

    <!-- Preliminary phase -->
    <g class="phase-heading">
      <text class="phase-title" x="290" y="282" font-size="18" textLength="104" lengthAdjust="spacingAndGlyphs">Preliminary</text>
      <rect class="tag-preliminary" x="395" y="269" width="46" height="14"/>
      <text class="phase-tag-text tag-text-dark" x="418" y="279.5">PHASE</text>
      <path class="guide" d="M262 294 V289 H404 V285"/>
    </g>

    <g class="step" transform="translate(232,294)">
      <use href="#stepCard" class="frame-preliminary" width="62" height="50"/>
      <g transform="translate(31,23)">
        <rect class="icon-line" x="-6" y="-8" width="12" height="15" rx="1"/>
        <path class="icon-stroke" d="M-3.5 -4 H3.5 M-3.5 -1 H3.5 M-3.5 2 H1"/>
        <path class="icon-stroke" d="M1 6 L8 -3" stroke-width="1.6"/>
      </g>
      <rect class="step-label-box" x="11" y="44" width="40" height="17"/>
      <text class="step-label" x="31" y="51">PRELIMINARY</text>
      <text class="step-label" x="31" y="56.5">AGREEMENT</text>
      <text class="step-copy" x="31" y="67">
        <tspan x="31">A quick chat by phone or email to</tspan>
        <tspan x="31" dy="4.3">learn about your plans, then we send</tspan>
        <tspan x="31" dy="4.3">a short questionnaire so we can see</tspan>
        <tspan x="31" dy="4.3">if we are a good match to work</tspan>
        <tspan x="31" dy="4.3">together.</tspan>
      </text>
    </g>
    <polygon class="flow-arrow" transform="translate(306,316)" points="0,-3.5 6,0 0,3.5"/>
    <g class="step" transform="translate(326,294)">
      <use href="#stepCard" class="frame-preliminary" width="62" height="50"/>
      <g transform="translate(31,23)">
        <path class="icon-stroke" d="M-10 6 H10 M-8 6 V-6 H8 V6 M-4 -6 V6 M0 -6 V6 M4 -6 V6 M-8 0 H8"/>
      </g>
      <rect class="step-label-box" x="11" y="44" width="40" height="17"/>
      <text class="step-label" x="31" y="51">CONCEPT</text>
      <text class="step-label" x="31" y="56.5">DRAWINGS</text>
      <text class="step-copy" x="31" y="67">
        <tspan x="31">Here we sit down to go deeper into</tspan>
        <tspan x="31" dy="4.3">your project and talk about how we</tspan>
        <tspan x="31" dy="4.3">can help you.</tspan>
      </text>
    </g>
    <polygon class="flow-arrow" transform="translate(398,316)" points="0,-3.5 6,0 0,3.5"/>
    <g class="step" transform="translate(418,294)">
      <use href="#stepCard" class="frame-preliminary" width="62" height="50"/>
      <g transform="translate(31,23)">
        <rect class="icon-line" x="-9" y="-6" width="18" height="12" rx="1"/>
        <path class="icon-stroke" d="M-6 -3 H1 M-6 0 H1 M-6 3 H1"/>
        <rect class="icon-fill" x="3" y="-3" width="4" height="6"/>
      </g>
      <rect class="step-label-box" x="11" y="44" width="40" height="17"/>
      <text class="step-label" x="31" y="51">UPDATED</text>
      <text class="step-label" x="31" y="56.5">ESTIMATE</text>
      <text class="step-copy" x="31" y="67">
        <tspan x="31">At this stage we give you a first</tspan>
        <tspan x="31" dy="4.3">estimate based on our early talks,</tspan>
        <tspan x="31" dy="4.3">so we can deliver the best possible</tspan>
        <tspan x="31" dy="4.3">home for your budget (2-3 days).</tspan>
      </text>
    </g>
    <polygon class="flow-arrow" transform="translate(488,364)" points="-3.5,0 3.5,0 0,6"/>

    <g class="step" transform="translate(232,394)">
      <use href="#stepCard" class="frame-preliminary" width="62" height="50"/>
      <g transform="translate(31,23)">
        <rect class="icon-line" x="-8" y="-7" width="11" height="14" rx="1" transform="rotate(-12)"/>
        <rect class="icon-line" x="-3" y="-7" width="11" height="14" rx="1"/>
        <path class="icon-stroke" d="M-1 -3 H6 M-1 0 H6 M-1 3 H4"/>
      </g>
      <rect class="step-label-box" x="11" y="44" width="40" height="17"/>
      <text class="step-label" x="31" y="51">SIGN</text>
      <text class="step-label" x="31" y="56.5">CONTRACT</text>
      <text class="step-copy" x="31" y="67">
        <tspan x="31">A quick chat by phone or email to</tspan>
        <tspan x="31" dy="4.3">learn about your plans, then we send</tspan>
        <tspan x="31" dy="4.3">a short questionnaire so we can see</tspan>
        <tspan x="31" dy="4.3">if we are a good match to work</tspan>
        <tspan x="31" dy="4.3">together.</tspan>
      </text>
    </g>
    <polygon class="flow-arrow" transform="translate(312,416)" points="0,-3.5 -6,0 0,3.5"/>
    <g class="step" transform="translate(326,394)">
      <use href="#stepCard" class="frame-preliminary" width="62" height="50"/>
      <g transform="translate(28,30)">
        <rect class="icon-line" x="-2" y="-16" width="5" height="16" transform="rotate(-30)"/>
        <rect class="icon-line" x="-2" y="-16" width="5" height="16" transform="rotate(0)"/>
        <rect class="icon-fill" x="-2" y="-16" width="5" height="16" transform="rotate(30)"/>
      </g>
      <rect class="step-label-box" x="11" y="44" width="40" height="17"/>
      <text class="step-label" x="31" y="51">COLOR</text>
      <text class="step-label" x="31" y="56.5">SELECTIONS</text>
      <text class="step-copy" x="31" y="67">
        <tspan x="31">Here we sit down to go deeper into</tspan>
        <tspan x="31" dy="4.3">your project and talk about how we</tspan>
        <tspan x="31" dy="4.3">can help you.</tspan>
      </text>
    </g>
    <rect class="progress-bar" x="398" y="394" width="7" height="46" fill="url(#stripes)"/>
    <g class="step" transform="translate(418,394)">
      <use href="#stepCard" class="frame-preliminary" width="62" height="50"/>
      <g transform="translate(31,23)">
        <rect class="icon-line" x="-9" y="-6" width="18" height="12" rx="1"/>
        <path class="icon-stroke" d="M-6 -3 H1 M-6 0 H1 M-6 3 H1"/>
        <rect class="icon-fill" x="3" y="-3" width="4" height="6"/>
      </g>
      <rect class="step-label-box" x="11" y="44" width="40" height="17"/>
      <text class="step-label" x="31" y="51">1ST BASE PAIDS</text>
      <text class="step-label" x="31" y="56.5">ESTIMATE</text>
      <text class="step-copy" x="31" y="67">
        <tspan x="31">At this stage we give you a first</tspan>
        <tspan x="31" dy="4.3">estimate based on our early talks,</tspan>
        <tspan x="31" dy="4.3">so we can deliver the best possible</tspan>
        <tspan x="31" dy="4.3">home for your budget (2-3 days).</tspan>
      </text>
    </g>

    <!-- Construction stage -->
    <g class="phase-heading">
      <text class="phase-title" x="275" y="515" font-size="18" textLength="118" lengthAdjust="spacingAndGlyphs">Construction</text>
      <rect class="tag-construction" x="395" y="502" width="46" height="14"/>
      <text class="phase-tag-text tag-text-light" x="418" y="512.5">STAGE</text>
      <path class="guide" d="M441 509 H458 V520"/>
    </g>

    <g class="step" transform="translate(232,526)">
      <use href="#stepCard" class="frame-construction" width="62" height="50"/>
      <rect class="step-label-box" x="11" y="44" width="40" height="17"/>
      <text class="step-label" x="31" y="51">INITIAL</text>
      <text class="step-label" x="31" y="56.5">CONTACT</text>
      <text class="step-copy" x="31" y="67">
        <tspan x="31">A quick chat by phone or email to</tspan>
        <tspan x="31" dy="4.3">learn about your plans, then we send</tspan>
        <tspan x="31" dy="4.3">a short questionnaire so we can see</tspan>
        <tspan x="31" dy="4.3">if we are a good match to work</tspan>
        <tspan x="31" dy="4.3">together.</tspan>
      </text>
    </g>
    <polygon class="flow-arrow" transform="translate(306,548)" points="0,-3.5 6,0 0,3.5"/>
    <g class="step" transform="translate(326,526)">
      <use href="#stepCard" class="frame-construction" width="62" height="50"/>
      <rect class="step-label-box" x="11" y="44" width="40" height="17"/>
      <text class="step-label" x="31" y="51">INITIAL</text>
      <text class="step-label" x="31" y="56.5">FACE TO FACE</text>
      <text class="step-copy" x="31" y="67">
        <tspan x="31">Here we sit down to go deeper into</tspan>
        <tspan x="31" dy="4.3">your project and talk about how we</tspan>
        <tspan x="31" dy="4.3">can help you.</tspan>
      </text>
    </g>
    <polygon class="flow-arrow" transform="translate(398,548)" points="0,-3.5 6,0 0,3.5"/>
    <g class="step" transform="translate(418,526)">
      <use href="#stepCard" class="frame-construction" width="62" height="50"/>
      <rect class="step-label-box" x="11" y="44" width="40" height="17"/>
      <text class="step-label" x="31" y="51">1ST BASE PAIDS</text>
      <text class="step-label" x="31" y="56.5">ESTIMATE</text>
      <text class="step-copy" x="31" y="67">
        <tspan x="31">At this stage we give you a first</tspan>
        <tspan x="31" dy="4.3">estimate based on our early talks,</tspan>
        <tspan x="31" dy="4.3">so we can deliver the best possible</tspan>
        <tspan x="31" dy="4.3">home for your budget (2-3 days).</tspan>
      </text>
    </g>
  </svg>
</div>
</body>
</html>
```